KORVELLA Corporate Business Card

Modern business card design for company which focuses in the areas of Staffing, IT Consulting & Data Services. Please note: We are no longer using the IT subscript on the logo. All designs should have IT subscript removed.
Website: www.korvellait.example

```html
<!DOCTYPE html>
<html lang="en">
<head>
<meta charset="utf-8">
<title>KORVELLA Business Card</title>
<link rel="stylesheet" href="https://fonts.googleapis.com/css2?family=Montserrat:wght@600;700&family=Roboto:wght@400&display=swap">
<style>
  :root {
    --bg: #3a3a3c;
    --navy: #064f86;
    --navy-light: #1c6fae;
    --brand-blue: #1a8fd6;
    --card-white: #f7f7f7;
    --ink: #3d3d3d;
    --divider: #1f7fc8;
  }
  html, body {
    margin: 0;
    width: 1200px;
    height: 1021px;
    overflow: hidden;
    background: var(--bg);
  }
  .stage { position: relative; width: 1200px; height: 1021px; }
  .card {
    position: absolute;
    left: 275px;
    width: 650px;
    height: 372px;
    box-shadow: 0 6px 18px rgba(0,0,0,.45);
    overflow: hidden;
  }
  /* Front */
  .card-front { top: 110px; background: var(--navy); }
  .front-texture {
    position: absolute; inset: 0;
    background: radial-gradient(ellipse at 55% 55%, var(--navy-light) 0%, rgba(28,111,174,.35) 45%, rgba(6,79,134,0) 75%);
  }
  .front-logo {
    position: absolute; left: 0; right: 0; top: 130px;
    text-align: center;
    font: 700 74px/1 "Montserrat", sans-serif;
    color: #f2f2f2;
    letter-spacing: 2px;
  }
  .front-url {
    position: absolute; left: 0; right: 0; top: 268px;
    text-align: center;
    font: 400 15px/1 "Roboto", sans-serif;
    color: #e6eef6;
    letter-spacing: 3px;
  }
  /* Back */
  .card-back { top: 540px; background: var(--card-white); }
  .back-logo {
    position: absolute; left: 48px; top: 135px;
    display: flex; align-items: center; gap: 10px;
    font: 700 46px/1 "Montserrat", sans-serif;
    color: var(--brand-blue);
  }
  .back-logo .mark { width: 26px; height: 26px; background: var(--brand-blue); }
  .divider {
    position: absolute; left: 350px; top: 100px;
    width: 2px; height: 140px; background: var(--divider);
  }
  .contact { position: absolute; left: 380px; top: 100px; color: var(--ink); }
  .contact-name { font: 700 25px/1.1 "Montserrat", sans-serif; color: var(--brand-blue); margin: 0; }
  .contact-role { font: 400 19px/1.2 "Roboto", sans-serif; margin: 2px 0 16px; }
  .contact-list { list-style: none; padding: 0; margin: 0; font: 400 19px/1.35 "Roboto", sans-serif; }
  .contact-list li { display: flex; align-items: center; gap: 8px; }
  .contact-list svg { width: 16px; height: 16px; flex: none; }
  .address {
    position: absolute; left: 0; right: 0; top: 300px;
    text-align: center;
    font: 400 20px/1 "Roboto", sans-serif;
    color: var(--ink);
  }
</style>
</head>
<body>
<div class="stage">
  <section class="card card-front">
    <div class="front-texture" role="img" aria-label="Blue field of scattered digital pixel squares"></div>
    <div class="front-logo">KORVELLA</div>
    <div class="front-url">www.korvellait.example</div>
  </section>

  <section class="card card-back">
    <div class="back-logo"><span class="mark"></span>KORVELLA</div>
    <div class="divider"></div>
    <div class="contact">
      <p class="contact-name">Daniel Reyes</p>
      <p class="contact-role">Founder</p>
      <ul class="contact-list">
        <li>
          <svg viewBox="0 0 16 16"><path fill="#3d3d3d" d="M3.5 1l2.5 3-1.5 1.8c.8 1.8 2.3 3.3 4.1 4.2L10.4 8.5l3.1 2.4-1.4 2.9C7 13.5 2.3 8.8 1.5 3.6z"/></svg>
          555-014-2290
        </li>
        <li>
          <svg viewBox="0 0 16 16"><rect x="1" y="3" width="14" height="10" fill="none" stroke="#3d3d3d" stroke-width="1.5"/><path d="M1 3l7 6 7-6" fill="none" stroke="#3d3d3d" stroke-width="1.5"/></svg>
          daniel@korvellait.example
        </li>
        <li>
          <svg viewBox="0 0 16 16"><circle cx="8" cy="8" r="6.5" fill="none" stroke="#3d3d3d" stroke-width="1.3"/><ellipse cx="8" cy="8" rx="3" ry="6.5" fill="none" stroke="#3d3d3d" stroke-width="1.1"/><path d="M1.5 8h13" stroke="#3d3d3d" stroke-width="1.1"/></svg>
          www.korvellait.example
        </li>
      </ul>
    </div>
    <div class="address">418 Harbor Ave,&nbsp; Lakeview, IN 46000</div>
  </section>
</div>
</body>
</html>
```